New signage for apartment community in the Pacific Northwest

Signage for an apartment community in the Pacific Northwest. It should have a contemporary northwest vibe with a fresh exciting feeling. We are open to the colors cayenne, white, charcoal and a splash of lime green. Sign to have the name 'VONTEL' with the address number 14727 smaller underneath. sign can include a shape under the name or a feeling of energy in the shape of the name.

Target Market(s)

Young urban professionals

Industry/Entity Type

Real Estate Development

Requirements
Must have
• eyecatching
Should not have
• anything too cute or too busy

```html
<!DOCTYPE html>
<html lang="en">
<head>
<meta charset="UTF-8">
<title>VONTEL Community Sign</title>
<link href="https://fonts.googleapis.com/css2?family=Open+Sans:wght@700;800&display=swap" rel="stylesheet">
<style>
  :root {
    --charcoal: #36434d;
    --lime: #00ff00;
    --white: #ffffff;
    --backdrop: #ecebe8;
  }
  html, body {
    margin: 0;
    padding: 0;
    width: 1200px;
    height: 2503px;
    overflow: hidden;
    background: var(--backdrop);
    font-family: "Open Sans", Arial, sans-serif;
  }
  .sign {
    position: absolute;
    left: 100px;
    top: 585px;
    width: 1000px;
    height: 1332px;
    background: var(--charcoal);
    overflow: hidden;
  }
  .sign__accent {
    position: absolute;
    inset: 0;
  }
  .name-plate {
    position: absolute;
    left: 48px;
    top: 138px;
    width: 902px;
    height: 451px;
    background: var(--white);
    border-radius: 26px;
    box-shadow: 0 26px 30px -14px rgba(0,0,0,0.55);
  }
  .name-plate__frame {
    position: absolute;
    inset: 20px;
    border: 3px solid var(--charcoal);
    border-radius: 12px;
  }
  .name-plate__title {
    position: absolute;
    left: 0;
    right: 0;
    top: 72px;
    margin: 0;
    text-align: center;
    font-weight: 800;
    font-size: 196px;
    line-height: 1;
    letter-spacing: -4px;
    color: var(--charcoal);
  }
  .address-pill {
    position: absolute;
    left: 174px;
    top: 325px;
    width: 564px;
    height: 75px;
    background: var(--lime);
    border-radius: 38px;
    display: flex;
    align-items: center;
    justify-content: center;
    gap: 12px;
    font-weight: 700;
    font-size: 38px;
    color: var(--charcoal);
    white-space: nowrap;
  }
  .address-pill svg { width: 26px; height: 34px; }
  .call-label {
    position: absolute;
    left: 0;
    right: 0;
    top: 920px;
    margin: 0;
    text-align: center;
    font-weight: 800;
    font-size: 112px;
    line-height: 1;
    color: var(--charcoal);
  }
  .phone-pill {
    position: absolute;
    left: 181px;
    top: 1059px;
    width: 684px;
    height: 143px;
    box-sizing: border-box;
    border: 5px solid var(--white);
    border-radius: 72px;
    background: linear-gradient(to bottom, #8a939a 0%, #4a5660 42%, var(--charcoal) 60%, #2c373f 100%);
    box-shadow: 0 6px 10px rgba(0,0,0,0.35);
    display: flex;
    align-items: center;
    justify-content: center;
    padding-left: 70px;
    font-weight: 800;
    font-size: 86px;
    letter-spacing: -1px;
    color: var(--white);
  }
  .phone-badge {
    position: absolute;
    left: 133px;
    top: 1082px;
    width: 105px;
    height: 105px;
    box-sizing: border-box;
    border-radius: 50%;
    background: var(--white);
    border: 4px solid var(--charcoal);
    box-shadow: 0 0 0 4px var(--white), 0 4px 8px rgba(0,0,0,0.35);
    display: flex;
    align-items: center;
    justify-content: center;
  }
  .phone-badge svg { width: 60px; height: 60px; }
</style>
</head>
<body>
  <main class="sign">
    <svg class="sign__accent" width="1000" height="1332" viewBox="0 0 1000 1332" aria-hidden="true">
      <polygon points="0,859 1000,596 1000,1332 0,1332" fill="var(--lime)"/>
    </svg>

    <section class="name-plate">
      <div class="name-plate__frame"></div>
      <h1 class="name-plate__title">VONTEL</h1>
      <div class="address-pill">
        <svg viewBox="0 0 24 32" aria-hidden="true">
          <path d="M12 2C6.5 2 3 6 3 11c0 7 9 19 9 19s9-12 9-19c0-5-3.5-9-9-9z" fill="none" stroke="var(--charcoal)" stroke-width="3.5"/>
          <circle cx="12" cy="11" r="3.5" fill="var(--charcoal)"/>
        </svg>
        <span>58310 Evergreen Ridgeway</span>
      </div>
    </section>

    <p class="call-label">Call Now</p>
    <div class="phone-pill">2064-318-557</div>
    <div class="phone-badge">
      <svg viewBox="0 0 24 24" aria-hidden="true">
        <path d="M6.6 3.5l2.6 3.2c.4.5.3 1.2-.1 1.6L7.6 9.7c1.2 2.6 3.5 4.9 6.1 6.1l1.4-1.5c.4-.4 1.1-.5 1.6-.1l3.2 2.6c.5.4.6 1.2.1 1.7l-1.7 1.9c-.6.6-1.5.9-2.4.6C9.4 19 4.9 14.5 3 8c-.3-.9 0-1.8.6-2.4l1.9-1.7c.3-.5 1.1-.5 1.1-.4z" fill="none" stroke="var(--charcoal)" stroke-width="2"/>
        <path d="M14 3.5a7 7 0 0 1 6.5 6.5M14 7a3.5 3.5 0 0 1 3 3" fill="none" stroke="var(--charcoal)" stroke-width="1.8" stroke-linecap="round"/>
      </svg>
    </div>
  </main>
</body>
</html>
```